Business Card Design

We need a business card design that can also be aplied for postcards. We are a small indie record company that also do consulting, and development of independat artitst . I already have the name and the basic idea of what i am looking for but i am open to any suggestion.
Info for the card
Name of the company : Velmora Records
NAME : Tomas Invaldi
PHONE : 208-5536142
EMAIL : hello@velmorarecords.example
WEB: www.velmorarecords.example
Target Market(s)
Male - Female independent musicians ages 18 to 45
Industry/Entity Type
Record Company
Contact Information for Business Card
Independant records company that also works in consulting for music business models for independent artists
Look and feel
Each slider illustrates characteristics of the customer's brand and the style your logo design should communicate.

```html
<!DOCTYPE html>
<html lang="en">
<head>
<meta charset="utf-8">
<title>Velmora Records – Business Card</title>
<link rel="stylesheet" href="https://fonts.googleapis.com/css2?family=Arimo:wght@700&display=swap">
<style>
  :root {
    --sky-blue: #4a9fc0;
    --sky-blue-light: #55a8c8;
    --deep-blue: #045684;
    --stripe-blue: #5a9cc6;
    --white: #ffffff;
  }
  html, body {
    margin: 0;
    padding: 0;
    width: 1200px;
    height: 704px;
    overflow: hidden;
    background: var(--white);
  }
  .card {
    position: relative;
    width: 1200px;
    height: 704px;
    overflow: hidden;
    font-family: "Arimo", Arial, sans-serif;
    font-weight: 700;
    color: var(--white);
    background: var(--deep-blue);
  }
  .texture-area {
    position: absolute;
    left: 0;
    top: 0;
    width: 1200px;
    height: 469px;
    background: linear-gradient(160deg, var(--sky-blue-light), var(--sky-blue));
  }
  .company-name {
    position: absolute;
    left: 0;
    top: 190px;
    width: 1200px;
    margin: 0;
    text-align: center;
    font-size: 84px;
    line-height: 1;
    font-weight: 700;
    letter-spacing: 0.5px;
  }
  .contact-band {
    position: absolute;
    left: 0;
    top: 469px;
    width: 1200px;
    height: 193px;
    background: var(--deep-blue);
  }
  .person-name {
    position: absolute;
    left: 57px;
    top: 543px;
    margin: 0;
    font-size: 46px;
    line-height: 1;
  }
  .contact-divider {
    position: absolute;
    left: 637px;
    top: 567px;
    width: 563px;
    height: 3px;
    background: var(--white);
  }
  .contact-line {
    position: absolute;
    left: 640px;
    width: 556px;
    margin: 0;
    text-align: center;
    line-height: 1;
  }
  .contact-email { top: 521px; font-size: 28px; }
  .contact-web { top: 585px; font-size: 28px; }
  .contact-phone { top: 628px; font-size: 26px; }
  .footer-stripe {
    position: absolute;
    left: 0;
    top: 662px;
    width: 1200px;
    height: 21px;
  }
</style>
</head>
<body>
  <div class="card">
    <div class="texture-area" role="img" aria-label="Subtle blue herringbone background texture"></div>
    <h1 class="company-name">Velmora Records</h1>

    <div class="contact-band"></div>
    <p class="person-name">Tomas Invaldi</p>
    <p class="contact-line contact-email">hello@velmorarecords.example</p>
    <div class="contact-divider"></div>
    <p class="contact-line contact-web">www.velmorarecords.example</p>
    <p class="contact-line contact-phone">208-5536142</p>

    <svg class="footer-stripe" viewBox="0 0 1200 21" preserveAspectRatio="none" aria-hidden="true">
      <rect x="0" y="0" width="1200" height="21" fill="var(--stripe-blue)"/>
      <polygon points="516,0 1200,0 1200,21 494,21" fill="var(--white)"/>
    </svg>
  </div>
</body>
</html>
```